Design and brand an anti cellulite cream.
Brand is Vorelle
Product name - PPC Cream and Cellulite Smoother.
Have uploaded the packaging it will be in - will be either white with silver/grey printing or Black with white writing.
No logo just really clean modern font that stands out
Want something modern, clean, slick and classy. Think Brissot/Velmo.
Want it to stand out on shelf and look amazing

Love the look of this product of the Dulce Petal Pout -

The Vorelle could be a grey as the Dulce -
PPC Cream and Cellulite Smoother in grey as -Petal pout
In pink - Target early and stubborn cellulite
200ml in grey
Updates

Vorelle is the brand - Renewa is the product name - PPC cream & cellulite smoother is the tag line.

I don't want to see Vorelle and Renewa together on the same line... I want Vorelle to stand out as the brand name and then the word Renewa PPC cream and cellulite smoother explain the product and I want to see it designed on the bottle that I provided. Thanks

Reason: more time for designers to put their designers on the bottles that I uploaded and please remember that Vorelle is the brand name not Vorelle Renewa - Renewa PPC cream and cellulite smoother needs to be a bit smaller than the vorelle word as most of the designs have Vorelle Renewa the same size and that is not what the product is called

Hi everyone, I have decided to take the word Renewa out as it is looking very busy. Brans id Vorelle - this needs to stand out - Product name is PPC Cream & Cellulite Smoother

The front of  bottle also needs to include in it's lay out

Targets early and stubborn cellulite.

200ml

I have added a picture of a product from Dulce because I like the look of this product and would like to see Vorelle done in this look

Vorelle in grey as Dulce/.... PPC Cream and Cellulite Smoother in grey as Kissable Lips/ ... Target early and stubborn cellulite in pink as smoothing lip exfoliant/ 200ml in grey

Could do a similar look with the black packaging with white and another soft colour                                   

Target Market(s)

Women - tho men can use it

Industry/Entity Type

Printing

Logo Text

Vorelle PPC Cream & Cellulite Smoother

Logo styles of interest
Lettermark Logo
Requirements
Must have
• Vorelle is the brand so would like that to stand out - PPC Cream and Cellulite Smoother is the mane of the product

```html
<!DOCTYPE html>
<html lang="en">
<head>
<meta charset="utf-8">
<title>Vorelle – PPC Cream &amp; Cellulite Smoother – Packaging Options</title>
<link rel="stylesheet" href="https://fonts.googleapis.com/css2?family=Josefin+Sans:wght@300&family=Ubuntu:ital,wght@0,400;1,700&display=swap">
<style>
  :root {
    --backdrop: #dcdcd8;
    --tube-white: #f4f3f1;
    --tube-white-shade: #e2e0dc;
    --cap-white: #eeede9;
    --tube-black: #141317;
    --cap-black: #0c0c0e;
    --ink-grey: #2b2b2e;
    --ink-white: #ffffff;
    --accent-pink: #d6365e;
    --tag-yellow: #fff200;
    --tag-ink: #111111;
  }
  * { margin: 0; padding: 0; box-sizing: border-box; }
  html, body { width: 1200px; height: 1000px; overflow: hidden; }
  body { background: var(--backdrop); position: relative; }

  .packaging-art { position: absolute; inset: 0; }

  .label { position: absolute; inset: 0; }
  .brand-name {
    position: absolute;
    font-family: "Josefin Sans", sans-serif;
    font-weight: 300;
    font-size: 42px;
    letter-spacing: 2px;
    text-align: center;
    line-height: 1;
    white-space: nowrap;
  }
  .product-name {
    position: absolute;
    font-family: "Ubuntu", sans-serif;
    font-style: italic;
    font-weight: 700;
    font-size: 23px;
    line-height: 31px;
    padding: 8px 0 6px;
    border-top: 2px solid;
    border-bottom: 2px solid;
    width: 258px;
    white-space: nowrap;
  }
  .tagline {
    position: absolute;
    font-family: "Josefin Sans", sans-serif;
    font-weight: 300;
    font-size: 18px;
    line-height: 21px;
    color: var(--accent-pink);
    text-transform: uppercase;
    white-space: nowrap;
  }
  .volume {
    position: absolute;
    font-family: "Ubuntu", sans-serif;
    font-size: 15px;
    white-space: nowrap;
  }

  .option-white .brand-name { left: 140px; top: 238px; width: 265px; color: var(--ink-grey); }
  .option-white .product-name { left: 145px; top: 418px; color: var(--ink-grey); border-color: var(--ink-grey); }
  .option-white .tagline { left: 145px; top: 512px; }
  .option-white .volume { left: 342px; top: 708px; color: var(--ink-grey); }

  .option-black .brand-name { left: 770px; top: 630px; width: 260px; color: var(--ink-white); }
  .option-black .product-name { left: 775px; top: 296px; width: 229px; color: var(--ink-white); border-color: var(--ink-white); }
  .option-black .tagline { left: 773px; top: 395px; }
  .option-black .volume { left: 773px; top: 453px; color: var(--ink-white); }
</style>
</head>
<body>
  <svg class="packaging-art" width="1200" height="1000" viewBox="0 0 1200 1000" aria-hidden="true">
    <defs>
      <linearGradient id="white-tube-shade" x1="0" x2="1" y1="0" y2="0">
        <stop offset="0" stop-color="var(--tube-white-shade)"/>
        <stop offset="0.35" stop-color="var(--tube-white)"/>
        <stop offset="1" stop-color="var(--tube-white-shade)"/>
      </linearGradient>
    </defs>

    <rect class="cap" x="178" y="850" width="206" height="100" rx="6" fill="var(--cap-white)"/>
    <path class="tube" d="M160 865 C130 800 120 700 120 600 L120 200 Q120 85 240 85 L320 85 Q440 85 440 200 L440 600 C440 700 430 800 400 865 Z" fill="url(#white-tube-shade)"/>

    <rect class="cap" x="805" y="780" width="190" height="140" rx="6" fill="var(--cap-black)"/>
    <path class="tube" d="M782 795 C752 720 740 600 740 500 L745 150 Q750 20 860 20 L940 20 Q1050 20 1055 150 L1060 500 C1060 620 1045 730 1012 795 Z" fill="var(--tube-black)"/>

    <polygon points="0,0 140,0 0,140" fill="var(--tag-yellow)"/>
    <text x="60" y="62" transform="rotate(-45 60 62)" text-anchor="middle" font-family="Ubuntu, sans-serif" font-size="26" fill="var(--tag-ink)">Option 1</text>
    <polygon points="1200,1000 1060,1000 1200,860" fill="var(--tag-yellow)"/>
    <text x="1142" y="952" transform="rotate(-45 1142 952)" text-anchor="middle" font-family="Ubuntu, sans-serif" font-size="26" fill="var(--tag-ink)">Option 2</text>
  </svg>

  <section class="label option-white">
    <h1 class="brand-name">VORELLE</h1>
    <h2 class="product-name">PPC Cream &amp;<br>Cellulite Smoother</h2>
    <p class="tagline">Target early and<br>stubborn cellulite</p>
    <p class="volume">200ml</p>
  </section>

  <section class="label option-black">
    <h2 class="product-name">PPC Cream &amp;<br>Cellulite Smoother</h2>
    <p class="tagline">Target early and<br>stubborn cellulite</p>
    <p class="volume">200ml</p>
    <h1 class="brand-name">VORELLE</h1>
  </section>
</body>
</html>
```